Great national branding opportunity

I am wanting a label created for a salsa brand I would like to launch. Full rendering of the label on the jar would be my end goal form this service. This will be called FiestaRidge Salsa (Greetings from FiestaRidge may be neat)

I am wanting something that sticks out on the shelf as well as fits our branding. holafiestaridge.example

We are in the beginning stage of growth and anticipate several more locations this year, so product development and conceptual design are important to us.

Target Market(s)

27-47, both male and female with average income from 40-70k. I would like to keep this authentic to San Antonio. Basically I am appealing to tourist as well as those traveling on business.

Industry/Entity Type

Restaurant

Logo Text

Greetings From, FiestaRidge, Red Salsa (Basically I want the parchment style background with our logo slanted as a watermark, while incorporating the other 2 attachments)

Logo styles of interest
Emblem Logo
Requirements
Must have
• Attractive food labeling. Parchment background with logo slanted as watermark. FiestaRidge, Red Salsa. I would like to see "natural" and/or "locally sourced" on the lid or some part of the packaging
Nice to have
• These are the highest competitors in my market: Pomarosa, Dwayne's, and Copper Kettle- I am attaching the photos below.

```html
<!DOCTYPE html>
<html lang="en">
<head>
<meta charset="utf-8">
<title>FiestaRidge Red Salsa Label</title>
<link href="https://fonts.googleapis.com/css2?family=Oswald:wght@700&display=swap" rel="stylesheet">
<style>
  :root {
    --page: #ffffff;
    --parchment-light: #f6efe0;
    --parchment-mid: #e9dcc0;
    --parchment-deep: #d8c49c;
    --parchment-edge: #c9ad72;
    --ink: #111111;
    --salsa-red: #c8123f;
    --pepper-red: #b5122e;
  }
  html, body {
    margin: 0;
    padding: 0;
    width: 1200px;
    height: 1000px;
    overflow: hidden;
    background: var(--page);
  }
  .canvas {
    position: relative;
    width: 1200px;
    height: 1000px;
  }
  .label {
    position: absolute;
    left: 310px;
    top: 220px;
    width: 580px;
    height: 548px;
    filter: drop-shadow(0 3px 4px rgba(0,0,0,0.18));
  }
  .brand-name,
  .product-name,
  .claim {
    font-family: "Oswald", "Arial Narrow", sans-serif;
    font-weight: 700;
  }
  .brand-name { fill: var(--ink); }
  .product-name { fill: var(--salsa-red); }
  .claim { fill: var(--ink); letter-spacing: 2px; }
</style>
</head>
<body>
<main class="canvas">
  <svg class="label" viewBox="0 0 365 345" xmlns="http://www.w3.org/2000/svg">
    <defs>
      <linearGradient id="parchment-fill" x1="0" y1="0" x2="1" y2="1">
        <stop offset="0" stop-color="var(--parchment-mid)"/>
        <stop offset="0.35" stop-color="var(--parchment-light)"/>
        <stop offset="0.7" stop-color="var(--parchment-mid)"/>
        <stop offset="1" stop-color="var(--parchment-deep)"/>
      </linearGradient>
      <linearGradient id="pepper-fill" x1="0" y1="0" x2="1" y2="0">
        <stop offset="0" stop-color="var(--pepper-red)"/>
        <stop offset="1" stop-color="#e0304f"/>
      </linearGradient>
    </defs>

    <path class="parchment"
      fill="url(#parchment-fill)" stroke="var(--parchment-edge)" stroke-width="0.8"
      d="M6 4 L40 0 L62 6 L95 2 L130 7 L160 1 L200 5 L238 0 L270 6 L300 2 L334 5 L362 2
         L358 30 L365 58 L360 92 L364 128 L358 160 L363 196 L359 232 L365 268 L360 300 L364 340
         L330 336 L300 342 L265 337 L232 343 L196 338 L160 344 L124 338 L92 343 L60 337 L28 342 L2 338
         L6 305 L0 272 L5 238 L1 202 L7 168 L2 134 L6 100 L0 66 L5 34 Z"/>

    <rect class="pepper" role="img" aria-label="Illustration of a red chili pepper with green stem"
      x="52" y="42" width="260" height="40" rx="20" fill="url(#pepper-fill)"/>

    <text class="brand-name" x="182" y="178" font-size="74" text-anchor="middle"
      textLength="318" lengthAdjust="spacingAndGlyphs">FIESTARIDGE</text>

    <text class="product-name" x="182" y="256" font-size="54" text-anchor="middle">RED SALSA</text>

    <text class="claim" x="182" y="306" font-size="14" text-anchor="middle">NATURAL · LOCALLY SOURCED</text>
  </svg>
</main>
</body>
</html>
```